Business Card Design

I need a design/ business card for a new company that caters for Event Hire (decorations and linen only) I am dabbling in rustic/ vintage designs for weddings and would like an elegant look to the cards. Something that will catch peoples eyes amongst the rest of the competitions cards and stand out to all fields, corporate/ weddings and general functions.

I am unsure of colours or pictures i would like so i am open to anything but possibly stick away from photos as i they are not more work of art on the card?

Target Market(s)

weddings and corporate events

Industry/Entity Type

Business

Contact Information for Business Card

Marlowe Weddings & Event Hire

Servicing the Gladstone Region for Weddings, Corporate & Private Functions

marloweweddings@postvane.com
Phone: 0427 813 542

Requirements
Must have
• The writing "Marlowe Weddings & Event Hire" please
Nice to have
• Something that really stands out as a must have at your event
Should not have
• Pictures that are not of my work

```html
<!DOCTYPE html>
<html lang="en">
<head>
<meta charset="utf-8">
<title>Marlowe Weddings &amp; Event Hire – Business Card</title>
<link rel="stylesheet" href="https://fonts.googleapis.com/css2?family=Crimson+Pro:wght@400&display=swap">
<style>
  :root {
    --card-light: #e4e9e5;
    --card-mid: #d3dad5;
    --ink: #343c3f;
    --ink-soft: #3f474a;
  }
  * { margin: 0; padding: 0; box-sizing: border-box; }
  html, body {
    width: 1200px;
    height: 741px;
    overflow: hidden;
    background: var(--card-light);
  }
  .card {
    position: relative;
    width: 1200px;
    height: 741px;
    overflow: hidden;
    font-family: "Crimson Pro", "Times New Roman", serif;
    font-weight: 400;
    color: var(--ink);
  }
  .card__grain {
    position: absolute;
    inset: 0;
    background: linear-gradient(180deg, var(--card-light) 0%, var(--card-mid) 55%, var(--card-light) 100%);
  }
  .brand {
    position: absolute;
    left: 0;
    right: 0;
    top: 150px;
    text-align: center;
    color: var(--ink);
  }
  .brand__name {
    display: block;
    font-size: 104px;
    line-height: 1;
    letter-spacing: 4px;
  }
  .brand__tagline {
    display: block;
    margin-top: 34px;
    font-size: 30px;
    line-height: 1.2;
    letter-spacing: 5px;
  }
  .service {
    position: absolute;
    left: 0;
    right: 0;
    top: 488px;
    text-align: center;
    font-size: 23px;
    line-height: 28px;
    color: var(--ink-soft);
  }
  .contact {
    position: absolute;
    top: 592px;
    text-align: center;
    color: var(--ink-soft);
  }
  .contact--email { left: 442px; transform: translateX(-50%); }
  .contact--phone { left: 830px; transform: translateX(-50%); }
  .contact__label {
    display: block;
    font-size: 22px;
    line-height: 26px;
    letter-spacing: 2px;
  }
  .contact__value {
    display: block;
    font-size: 18px;
    line-height: 26px;
    white-space: nowrap;
  }
  .contact--phone .contact__value {
    font-size: 20px;
    letter-spacing: 3px;
  }
</style>
</head>
<body>
  <div class="card">
    <div class="card__grain" role="img" aria-label="Pale whitewashed timber board background"></div>

    <h1 class="brand">
      <span class="brand__name">Marlowe</span>
      <span class="brand__tagline">Weddings &amp;<br>Event Hire</span>
    </h1>

    <p class="service">Servicing the Gladstone Region<br>Weddings, Corporate &amp; Private Functions</p>

    <div class="contact contact--email">
      <span class="contact__label">e-mail</span>
      <span class="contact__value">marloweweddings@postvane.com</span>
    </div>

    <div class="contact contact--phone">
      <span class="contact__label">phone</span>
      <span class="contact__value">0427 813 542</span>
    </div>
  </div>
</body>
</html>
```